Summit Leadership Renewal Roadmap

I've included a mock up of what I like. This design needs to be made better. I like the top section layout. It needs 5 circles for:

Please create a webpage based on this design, but improve it. Use the letterhead and business card brand you created for me to make the brand look seamless.

I love the circles - please make 5 of them the same size (can be 1 lines)

Here is the text for the circles:

Headline: Your Guided Path to Transformation
Text
Step 1: The Initial Consultation
text
Step 2: Deep-Dive Discovery and Assessment
text
Step 3: Synthesis and Strategy Formulation
text
Step 4: The Strategic Debrief Session
Text
Step 5: Implementation and Ongoing Support
Text

Also, there are many sections to this page including:

Introduction
Copy
Copy
Bio
CTA
FAQ's

Please make it interesting.

Use the colors of the mockup and my website: Corinna Halvard.com
I am including my letterhead and business card for brand coherence.

Use the fonts on my website. CorinnaHalvard.com

I will need all files to send to the developer. We must have ALL the art files.

Target Market(s)

see my website; CorinnaHalvard.com

Industry/Entity Type

See my uploads

Requirements
Must have
• all the design files

```html
<!DOCTYPE html>
<html lang="en">
<head>
<meta charset="utf-8">
<title>Summit Leadership Renewal — Corinna Halvard</title>
<link href="https://fonts.googleapis.com/css2?family=Epilogue:wght@300;400;500&display=swap" rel="stylesheet">
<style>
:root{
  --navy:#0d1840;
  --panel:#24336f;
  --lavender:#7b80b0;
  --gold:#d4ab52;
  --paper:#e9e9e7;
  --ink:#141c3c;
  --white:#ffffff;
}
*{box-sizing:border-box;margin:0;padding:0}
html,body{width:1200px;height:2776px;overflow:hidden}
body{position:relative;background:var(--paper);font-family:"Epilogue",sans-serif;color:var(--ink)}
.abs{position:absolute}
.btn{position:absolute;display:flex;align-items:center;justify-content:center;background:var(--gold);color:var(--white);font-size:11px;text-decoration:underline;letter-spacing:-.2px}
.placeholder{position:absolute}

/* hero */
.hero-left{left:0;top:0;width:329px;height:1089px;background:var(--navy)}
.hero-panel{left:329px;top:0;width:539px;height:625px;background:var(--panel);overflow:hidden}
.hero-right{left:868px;top:0;width:332px;height:1525px;background:var(--navy)}
.nav{left:329px;top:28px;width:539px;display:flex;justify-content:center;gap:27px;font-size:12px;color:var(--white)}
.brand{left:0;width:329px;text-align:center;color:var(--white)}
.brand-mark{display:block;margin:0 auto 14px;width:64px;height:64px;border-radius:50%;border:2px solid var(--gold)}
.brand-name{font-size:21px;letter-spacing:1px;font-weight:400}
.brand-sub{font-size:12px;letter-spacing:2px;color:var(--white);margin-top:4px}
.portrait-ring{left:65px;top:227px;width:198px;height:198px;border-radius:50%;border:3px solid var(--gold);background:radial-gradient(circle at 50% 40%,#e1bd6a,#c89b43)}
.coach-name{left:0;top:442px;width:329px;text-align:center;font-size:30px;color:var(--white);font-weight:400}
.coach-cred{left:0;top:481px;width:329px;text-align:center;font-size:11px;color:#c6c9dc}
.hero-title{left:914px;top:172px;width:280px;font-size:36px;line-height:41px;color:var(--white);font-weight:400;letter-spacing:-1px}
.hero-title span{color:var(--gold);white-space:nowrap;text-decoration:underline;text-decoration-thickness:2px;text-underline-offset:5px}
.hero-sub{left:913px;top:366px;width:250px;font-size:13px;line-height:19px;color:var(--white)}

/* process */
.process{left:22px;top:625px;width:1156px;height:494px;background:#e8e8e6}
.process-title{left:0;top:42px;width:1156px;text-align:center;font-size:32px;font-weight:400;color:var(--ink)}
.step-label{position:absolute;width:200px;text-align:center;font-size:16px;line-height:19px;color:var(--ink)}
.process svg{position:absolute;left:0;top:0}

/* about */
.about{left:0;top:1089px;width:868px;height:436px;background:var(--lavender)}
.about-title{left:93px;top:1192px;font-size:30px;color:var(--white);font-weight:400}
.about-photo{left:93px;top:1254px;width:168px;height:212px;background:linear-gradient(160deg,#8a93b5,#3b4474 60%,#1f2750)}
.about-photo span{position:absolute;left:0;bottom:16px;width:100%;text-align:center;color:var(--white);font-size:16px}
.about-copy{left:286px;top:1252px;width:528px;font-size:11px;line-height:16px;color:var(--white);font-weight:300;letter-spacing:-.2px}
.about-copy p+p{margin-top:13px}
.tagline-brand{left:868px;top:1180px;width:332px;text-align:center;color:var(--gold);font-size:13px;letter-spacing:2px}
.tagline{left:910px;top:1283px;width:270px;font-size:29px;line-height:30px;color:var(--white);font-weight:400}

/* seeking */
.seek-title{left:99px;top:1617px;width:600px;font-size:30px;line-height:34px;font-weight:400;color:var(--ink)}
.seek-copy{left:99px;top:1733px;width:570px;font-size:11px;line-height:16px;color:#3a3f55;font-weight:300}
.seek-copy b{font-weight:400;color:var(--ink)}
.sunrise{left:757px;top:1525px;width:443px;height:330px;background:radial-gradient(circle at 52% 58%,#fff3c4 0,#f5b844 12%,#c9793b 32%,#5e6a8c 62%,#3b5b8d 100%)}
.rule{left:99px;top:1855px;width:1101px;height:1px;background:#c9c9c9}

/* faq */
.lodge{left:105px;top:1933px;width:398px;height:499px;background:linear-gradient(170deg,#4d6b2d,#8aa84a 45%,#a9783f 70%,#5f7a34);z-index:2}
.faq-title{left:584px;top:1958px;font-size:30px;font-weight:400;color:var(--ink)}
.faq-item{position:absolute;left:586px;width:508px;height:52px;border:1px solid var(--ink);display:flex;align-items:center;justify-content:space-between;padding:0 12px 0 13px;font-size:13px;color:var(--ink)}
.faq-plus{width:26px;height:26px;background:var(--navy);color:var(--white);display:flex;align-items:center;justify-content:center;font-size:17px}
.to-top{left:1120px;top:2357px;width:46px;height:46px;border-radius:50%;background:var(--gold);z-index:3}

/* footer */
.footer{left:0;top:2380px;width:1200px;height:353px;background:var(--navy)}
.foot-head{position:absolute;font-size:18px;color:var(--white);font-weight:400}
.foot-list{position:absolute;font-size:11px;line-height:22px;color:#cfd2e2;list-style:none;font-weight:300}
.foot-about{left:467px;top:2573px;width:205px;font-size:11px;line-height:16px;color:#cfd2e2;font-weight:300}
.legal{left:0;top:2733px;width:1200px;height:43px;background:var(--lavender)}
.legal p{position:absolute;left:0;top:16px;width:1200px;text-align:center;font-size:11px;color:var(--white);font-weight:300}
.social{left:1071px;top:2745px;width:20px;height:20px;border-radius:50%;background:var(--white)}
</style>
</head>
<body>

<!-- hero -->
<div class="abs hero-left"></div>
<div class="abs hero-right"></div>
<div class="abs hero-panel">
  <svg width="539" height="625" viewBox="0 0 539 625">
    <defs>
      <linearGradient id="heroPhoto" x1="0" y1="0" x2="0" y2="1">
        <stop offset="0" stop-color="#3a6e9a"/>
        <stop offset=".55" stop-color="#b88a6a"/>
        <stop offset="1" stop-color="#1c2647"/>
      </linearGradient>
    </defs>
    <circle cx="269" cy="296" r="197" fill="none" stroke="var(--gold)" stroke-width="5"/>
    <g role="img" aria-label="Portrait of Corinna Halvard in a navy blazer, arms crossed">
      <path d="M92 296 A177 177 0 0 1 446 296 L446 625 L92 625 Z" fill="url(#heroPhoto)"/>
    </g>
  </svg>
</div>
<nav class="abs nav"><span>Coaching</span><span>Retreats</span><span>About</span><span>Insights</span><span>Contact</span></nav>

<div class="abs brand" style="top:36px">
  <span class="brand-mark"></span>
  <div class="brand-name">SUMMIT LEADERSHIP</div>
  <div class="brand-sub">RENEWAL</div>
</div>
<div class="abs portrait-ring" role="img" aria-label="Headshot of Corinna Halvard"></div>
<h1 class="abs coach-name">Corinna Halvard</h1>
<p class="abs coach-cred">M.A, ABS Founder, CEO</p>

<h2 class="abs hero-title">Support Your Leadership Efforts with <span>Elite Coaching</span></h2>
<p class="abs hero-sub">Introducing Elite Leadership Coaching and Organization Development</p>
<a class="btn" style="left:913px;top:432px;width:243px;height:39px">Book a Discovery Call</a>

<!-- process -->
<section class="abs process">
  <h2 class="abs process-title">Your Guided Path to Transformation</h2>
  <svg width="1156" height="494" viewBox="0 0 1156 494" fill="none">
    <g stroke="var(--ink)" stroke-width="3" stroke-linecap="round">
      <path d="M285 287 A84 84 0 1 1 285 243"/>
      <path d="M472 287 A84 84 0 1 1 472 243"/>
      <path d="M658 287 A84 84 0 1 1 658 243"/>
      <path d="M845 287 A84 84 0 1 1 845 243"/>
      <path d="M1032 287 A84 84 0 1 1 1032 243"/>
      <path d="M285 243 Q296 265 300 265"/>
      <path d="M472 243 Q483 265 487 265"/>
      <path d="M658 243 Q669 265 673 265"/>
      <path d="M845 243 Q856 265 860 265"/>
    </g>
    <g fill="var(--ink)">
      <path d="M299 259 L309 265 L299 271 Z"/>
      <path d="M486 259 L496 265 L486 271 Z"/>
      <path d="M672 259 L682 265 L672 271 Z"/>
      <path d="M859 259 L869 265 L859 271 Z"/>
    </g>
    <g fill="var(--gold)">
      <circle cx="204" cy="265" r="65" role="img" aria-label="Consultation icon"/>
      <circle cx="391" cy="265" r="65" role="img" aria-label="Assessment icon"/>
      <circle cx="577" cy="265" r="65" role="img" aria-label="Strategy icon"/>
      <circle cx="764" cy="265" r="65" role="img" aria-label="Debrief icon"/>
      <circle cx="951" cy="265" r="65" role="img" aria-label="Implementation icon"/>
    </g>
    <g fill="var(--navy)">
      <circle cx="204" cy="349" r="11"/><circle cx="391" cy="181" r="11"/>
      <circle cx="577" cy="349" r="11"/><circle cx="764" cy="181" r="11"/>
      <circle cx="951" cy="349" r="11"/>
    </g>
    <g fill="#fff" font-family="Epilogue, sans-serif" font-size="13" text-anchor="middle">
      <text x="204" y="354">1</text><text x="391" y="186">2</text>
      <text x="577" y="354">3</text><text x="764" y="186">4</text>
      <text x="951" y="354">5</text>
    </g>
  </svg>
  <div class="step-label" style="left:291px;top:125px">Deep-Dive Discovery<br>and Assessment</div>
  <div class="step-label" style="left:664px;top:125px">The Strategic<br>Debrief Session</div>
  <div class="step-label" style="left:104px;top:376px">The Initial<br>Consultation</div>
  <div class="step-label" style="left:477px;top:376px">Synthesis and<br>Strategy Formulation</div>
  <div class="step-label" style="left:851px;top:376px">Implementation and<br>Ongoing Support</div>
</section>

<!-- about -->
<div class="abs about"></div>
<h2 class="abs about-title">About Corinna Halvard</h2>
<div class="abs about-photo" role="img" aria-label="Portrait of Corinna Halvard"><span>Corinna Halvard</span></div>
<div class="abs about-copy">
  <p>As a top leader, you deserve an elite partnership designed exclusively for you—especially when you need a woman you can count on. With a perspective rooted in both wisdom and empathy, I offer insights, intuition, and support that many male coaches simply cannot replicate.</p>
  <p>My mission is to guide high-performing leaders and their teams toward a state of peak performance defined by stress-free resilience, heightened productivity, and effortless flow. I founded Corinna Halvard Partners to provide effective, accelerated training that unlocks the highest levels of human potential. I am especially passionate about empowering executives and senior-level management to lead with clarity, impact, and well-being.</p>
</div>
<a class="btn" style="left:285px;top:1428px;width:242px;height:38px">Book a Discovery Call</a>
<div class="abs tagline-brand">SUMMIT LEADERSHIP RENEWAL</div>
<h2 class="abs tagline">Elite Leadership is the Secret to Lasting Organization...</h2>
<a class="btn" style="left:913px;top:1428px;width:243px;height:38px">Book a Discovery Call</a>

<!-- seeking -->
<h2 class="abs seek-title">Are you seeking a Leadership Coach and Organization Development Specialist to elevate your leadership impact?</h2>
<p class="abs seek-copy"><b>Elite Coaching with Corinna Halvard</b> — Your organization—and its challenges—are unlike any other. Generic training can only take your leaders so far. To achieve the profound, lasting impact your vision demands, you need a solution crafted specifically for you.</p>
<div class="placeholder sunrise" role="img" aria-label="Sunrise above the clouds"></div>
<div class="abs rule"></div>

<!-- faq -->
<div class="abs footer"></div>
<div class="placeholder lodge" role="img" aria-label="Aerial view of a forest lodge with a garden deck and umbrellas"></div>
<h2 class="abs faq-title">Frequently Asked Questions</h2>
<div class="faq-item" style="top:2010px">What is a Summit Leadership Renewal Retreat?<span class="faq-plus">+</span></div>
<div class="faq-item" style="top:2072px">Who is this retreat designed for — and is it right for me?<span class="faq-plus">+</span></div>
<div class="faq-item" style="top:2134px">What topics or themes are covered during the retreat?<span class="faq-plus">+</span></div>
<div class="faq-item" style="top:2195px">How long is the retreat and what is the format?<span class="faq-plus">+</span></div>
<a class="btn" style="left:586px;top:2276px;width:242px;height:38px">View All FAQ</a>
<div class="abs to-top">
  <svg width="46" height="46" viewBox="0 0 46 46"><path d="M19 25 l4 -4 l4 4" stroke="#fff" stroke-width="1.5" fill="none"/></svg>
</div>

<!-- footer -->
<div class="abs brand" style="left:131px;top:2517px">
  <span class="brand-mark"></span>
  <div class="brand-name">SUMMIT LEADERSHIP</div>
  <div class="brand-sub">RENEWAL</div>
</div>
<h3 class="foot-head" style="left:467px;top:2537px">About Us</h3>
<p class="abs foot-about">Summit Leadership Renewal is a trade name owned by Corinna Halvard Partners and The Resonant Wellbeing Institute.</p>
<h3 class="foot-head" style="left:728px;top:2537px">Quick Links</h3>
<ul class="foot-list" style="left:728px;top:2568px"><li>2026 Retreat</li><li>About</li><li>Insights</li></ul>
<h3 class="foot-head" style="left:894px;top:2537px">Support</h3>
<ul class="foot-list" style="left:895px;top:2568px"><li>Terms &amp; Policies</li><li>Membership Agreement</li><li>Contact</li></ul>

<div class="abs legal"><p>Copyright © 2025. All rights reserved.</p></div>
<div class="abs social"></div>

</body>
</html>
```